Business Card Design Project for - The Brackenfold Lawncare Company Ltd. We are a Landscape and garden

I would like designer to use all special glosses etc so i can have a professional looking business card. The theme of the business card can reflect that of the Logo attached by ArtVellum or your own unique ideas.. please feel free to go wild as i hope i can select a winner i like - my budget will be committed so please get involved. Good luck and thank you Neville

Target Market(s)

Must look Professional

General Public and Businesses including Councils, Local Government, Hospitals, Hotels, Professionals and Professional Sports People.

Industry/Entity Type

Landscape Gardening

Contact Information for Business Card

The Brackenfold Lawncare Company Ltd

Mr R.P Ashworth
Head Office - Quayline Park Manchester
t. 0772 458 916
e. info@brackenfoldlawn.co.uk
w. www.brackenfoldlawn.co.uk

Facebook - https://www.pagemural.com/TheBrackenfoldLawncareCompany/
Twitter - https://chirpline.com/ThePlotTruck
Instagram - https://www.snapquilt.com/thebrackenfoldlawncarecompany/?hl=en
Google+ - https://circles.vondarix.com/u/0/208475932610482739516
Yelp - https://www.localrava.co.uk/biz/the-brackenfold-lawncare-company-manchester-4

Font styles to use
Serif
Script
Other font styles liked:
• I don't have much of an idea of font types sorry

Colors

Designer to choose colors to be used in the design.

Requirements
Must have
• A Professional look and Design
• Special effects with gloss and fading of colours possibly..
• Front and back design
Nice to have
• All special features with effects and gloss etc

```html
<!DOCTYPE html>
<html lang="en">
<head>
<meta charset="utf-8">
<title>The Brackenfold Lawncare Company Ltd – Business Card</title>
<link rel="stylesheet" href="https://fonts.googleapis.com/css2?family=Cinzel:wght@400;600&family=Roboto:wght@400;500&display=swap">
<style>
  :root {
    --backdrop: #4b4b4d;
    --card-black: #0c0c0d;
    --card-sheen: #2a2a2c;
    --leaf-green: #3fb93a;
    --lime: #b6e83c;
    --silver: #c9cbcf;
    --text-light: #f1f1f1;
    --text-dark: #1a1a1a;
    --dot-red: #d6262f;
    --dot-blue: #1d8fe0;
    --dot-purple: #b4338f;
    --dot-navy: #2f5fb8;
  }
  * { margin: 0; padding: 0; box-sizing: border-box; }
  html, body { width: 1200px; height: 852px; overflow: hidden; }
  body {
    position: relative;
    background: var(--backdrop);
    font-family: "Roboto", Arial, sans-serif;
  }
  .card {
    position: absolute;
    width: 500px;
    height: 286px;
    border-radius: 16px;
    overflow: hidden;
    background: linear-gradient(125deg, var(--card-sheen) 0%, var(--card-black) 45%, #161617 70%, var(--card-black) 100%);
    box-shadow: 0 12px 30px rgba(0,0,0,.45);
  }
  .card-back { left: 90px; top: 140px; }
  .card-front { left: 610px; top: 420px; }

  .wordmark { position: absolute; display: flex; align-items: center; gap: 12px; color: var(--silver); font-family: "Cinzel", Georgia, serif; font-weight: 400; }
  .wordmark-dot { width: 34px; height: 34px; border-radius: 50%; background: var(--leaf-green); flex: none; }
  .wordmark-name { line-height: 1.05; letter-spacing: 1px; }
  .wordmark-name .line-top { display: block; font-size: 26px; }
  .wordmark-name .line-bottom { display: block; font-size: 11px; letter-spacing: 3px; }

  .card-back .wordmark { right: 30px; top: 40px; }

  .social-links { position: absolute; left: 22px; bottom: 24px; list-style: none; }
  .social-links li { display: flex; align-items: center; gap: 8px; font-size: 11px; color: var(--text-light); line-height: 17px; }
  .net-dot { width: 11px; height: 11px; border-radius: 50%; flex: none; }
  .net-red { background: var(--dot-red); }
  .net-blue { background: var(--dot-blue); }
  .net-purple { background: var(--dot-purple); }
  .net-navy { background: var(--dot-navy); }

  .swoosh { position: absolute; left: 0; top: 0; width: 500px; height: 286px; }
  .holder { position: absolute; right: 26px; top: 16px; text-align: right; color: var(--text-dark); }
  .holder-name { font-family: "Cinzel", Georgia, serif; font-size: 17px; font-weight: 600; letter-spacing: 1px; }
  .holder-office { font-size: 11px; line-height: 14px; }

  .card-front .wordmark { left: 28px; top: 158px; gap: 10px; }
  .card-front .wordmark-dot { width: 30px; height: 30px; }
  .card-front .wordmark-name .line-top { font-size: 21px; }
  .card-front .wordmark-name .line-bottom { font-size: 9px; letter-spacing: 2.4px; }

  .contact-list { position: absolute; right: 22px; top: 160px; list-style: none; text-align: right; }
  .contact-list li { display: flex; justify-content: flex-end; align-items: center; gap: 7px; font-size: 11.5px; color: var(--text-light); line-height: 16px; }
  .contact-list svg { width: 11px; height: 11px; flex: none; }

  .follow { position: absolute; left: 38px; bottom: 20px; display: flex; align-items: center; gap: 6px; font-size: 11.5px; color: var(--text-light); }
  .follow .net-dot { width: 15px; height: 15px; }
  .follow-label { margin-right: 4px; }
</style>
</head>
<body>

<section class="card card-back" aria-label="Card back">
  <div class="wordmark">
    <span class="wordmark-dot"></span>
    <span class="wordmark-name"><span class="line-top">The Brackenfold</span><span class="line-bottom">Lawncare Company Ltd</span></span>
  </div>
  <ul class="social-links">
    <li><span class="net-dot net-red"></span>www.pagemural.com/TheBrackenfoldLawncareCompany/</li>
    <li><span class="net-dot net-blue"></span>chirpline.com/ThePlotTruck</li>
    <li><span class="net-dot net-purple"></span>www.snapquilt.com/thebrackenfoldlawncarecompany/?hl=en</li>
    <li><span class="net-dot net-red"></span>circles.vondarix.com/u/0/208475932610482739516</li>
    <li><span class="net-dot net-navy"></span>www.localrava.co.uk/biz/the-brackenfold-lawncare-company-manchester-4</li>
  </ul>
</section>

<section class="card card-front" aria-label="Card front">
  <svg class="swoosh" viewBox="0 0 500 286" aria-hidden="true">
    <defs>
      <linearGradient id="limeFade" x1="0" y1="1" x2="1" y2="0">
        <stop offset="0" stop-color="#27a83a"/>
        <stop offset="1" stop-color="#c4ec40"/>
      </linearGradient>
    </defs>
    <path d="M0 0 H500 V72 C380 80 200 94 0 112 Z" fill="url(#limeFade)"/>
    <path d="M0 112 C200 94 380 80 500 72 V84 C380 92 200 108 0 124 Z" fill="#0c0c0d"/>
    <path d="M0 124 C200 108 380 92 500 84 V92 C380 100 200 118 0 134 Z" fill="#4cc53a"/>
    <path d="M0 134 C160 118 300 104 430 96 C300 110 160 126 0 146 Z" fill="#2a9b36"/>
  </svg>
  <div class="holder">
    <div class="holder-name">MR R.P ASHWORTH</div>
    <div class="holder-office">Head Office<br>Quayline Park Manchester</div>
  </div>
  <div class="wordmark">
    <span class="wordmark-dot"></span>
    <span class="wordmark-name"><span class="line-top">The Brackenfold</span><span class="line-bottom">Lawncare Company Ltd</span></span>
  </div>
  <ul class="contact-list">
    <li>0772 458 916
      <svg viewBox="0 0 12 12" aria-hidden="true"><path d="M2 1 L4.5 1 L5.3 3.4 L4 4.4 C4.7 6 6 7.3 7.6 8 L8.6 6.7 L11 7.5 L11 10 C6 10.5 1.5 6 2 1 Z" fill="var(--leaf-green)"/></svg>
    </li>
    <li>info@brackenfoldlawn.co.uk
      <svg viewBox="0 0 12 12" aria-hidden="true"><rect x="1" y="2.5" width="10" height="7" fill="var(--leaf-green)"/><path d="M1 2.5 L6 6.5 L11 2.5" stroke="#0c0c0d" fill="none"/></svg>
    </li>
    <li>www.brackenfoldlawn.co.uk
      <svg viewBox="0 0 12 12" aria-hidden="true"><circle cx="6" cy="6" r="5" fill="var(--leaf-green)"/><path d="M1 6 H11 M6 1 C3.5 4 3.5 8 6 11 M6 1 C8.5 4 8.5 8 6 11" stroke="#0c0c0d" stroke-width=".8" fill="none"/></svg>
    </li>
  </ul>
  <div class="follow">
    <span class="follow-label">Follow us on</span>
    <span class="net-dot net-blue"></span>
    <span class="net-dot net-purple"></span>
    <span class="net-dot net-red"></span>
    <span class="net-dot net-navy"></span>
    <span class="net-dot net-red"></span>
  </div>
</section>

</body>
</html>
```